Real Estate Agency Chatterlane Cover Photo

We need a Chatterlane cover photo created for our Real Estate Business. We also need this cover photo adapted to several other platforms. Please read this brindlo doc for full specifications of the job https://files.brindlo-example.net/sheet/d/8QwerPLm4ZxVb2NnKs7RtYhUe3_gHdjAoFcWsMvBn/view?mode=share

Please also carefully read the Must Haves/Should Not Haves

Please contact me if you have any queries. Looking forward to seeing your designs!

Owen

Industry/Entity Type

Real Estate Agent

Requirements
Must have
• The Taglines 'More Money In Your Pocket' and sub tagline 'With Our Low Flat Fee To Sell Your Home'

It can then also have other elements e.g our logo, contact details and anything else you think will work well.

It must also have great graphic design work which looks custom and very clean/modern
Should not have
• Must not have poor quality stock images or anything tacky regarding money etc

```html
<!DOCTYPE html>
<html lang="en">
<head>
<meta charset="utf-8">
<title>Keyvale Cover Banners</title>
<link rel="stylesheet" href="https://fonts.googleapis.com/css2?family=Jost:wght@400;500;600&display=swap">
<style>
  :root {
    --stage: #4a4a4a;
    --stage-edge: #3c3c3c;
    --banner: #040404;
    --halftone-grey: #1c1c1c;
    --halftone-red: #2a0708;
    --ink: #ffffff;
    --accent: #e3141b;
  }
  html, body {
    margin: 0;
    padding: 0;
    width: 1200px;
    height: 1051px;
    overflow: hidden;
  }
  body {
    background: radial-gradient(ellipse at 50% 40%, var(--stage) 0%, var(--stage-edge) 100%);
    font-family: "Jost", "Futura", sans-serif;
    position: relative;
  }
  .cover {
    position: absolute;
    left: 46px;
    width: 1107px;
    height: 421px;
    background: var(--banner);
    box-shadow: 0 14px 40px rgba(0,0,0,0.55);
    overflow: hidden;
  }
  .cover--grey { top: 73px; }
  .cover--red { top: 560px; }
  .cover__texture {
    position: absolute;
    inset: 0;
  }
  .cover--grey .cover__texture {
    background: radial-gradient(ellipse 75% 110% at 0% 100%, var(--halftone-grey) 0%, rgba(28,28,28,0.4) 45%, rgba(4,4,4,0) 80%);
  }
  .cover--red .cover__texture {
    background: radial-gradient(ellipse 75% 110% at 0% 100%, var(--halftone-red) 0%, rgba(42,7,8,0.45) 45%, rgba(4,4,4,0) 80%);
  }
  .cover__content {
    position: absolute;
    left: 0;
    right: 0;
    top: 128px;
    text-align: center;
    color: var(--ink);
    padding-left: 10px;
  }
  .cover__headline {
    margin: 0;
    font-weight: 600;
    font-size: 53px;
    line-height: 1;
    letter-spacing: -0.3px;
  }
  .cover__tagline {
    margin: 14px 0 0;
    font-weight: 400;
    font-size: 30px;
    line-height: 1;
    letter-spacing: 0.2px;
  }
  .cover__contacts {
    display: flex;
    justify-content: center;
    align-items: center;
    gap: 18px;
    margin-top: 36px;
    font-size: 19px;
    font-weight: 500;
    letter-spacing: 0.3px;
  }
  .contact {
    display: flex;
    align-items: center;
    gap: 10px;
  }
  .contact__icon {
    width: 22px;
    height: 22px;
    flex: none;
  }
</style>
</head>
<body>

<section class="cover cover--grey">
  <div class="cover__texture" role="img" aria-label="Faint halftone dot pattern fading from the lower left corner"></div>
  <div class="cover__content">
    <h1 class="cover__headline">More Money In Your Pocket</h1>
    <p class="cover__tagline">With our Low Flat Fee To Sell Your Home</p>
    <div class="cover__contacts">
      <span class="contact">
        <svg class="contact__icon" viewBox="0 0 24 24" aria-hidden="true">
          <circle cx="12" cy="12" r="11" fill="var(--accent)"/>
          <g fill="none" stroke="#040404" stroke-width="1.1">
            <ellipse cx="12" cy="12" rx="4.5" ry="11"/>
            <line x1="12" y1="1" x2="12" y2="23"/>
            <line x1="1" y1="12" x2="23" y2="12"/>
            <path d="M3 6.5h18M3 17.5h18"/>
          </g>
        </svg>
        www.keyvale.com.au
      </span>
      <span class="contact">
        <svg class="contact__icon" viewBox="0 0 24 24" aria-hidden="true">
          <path fill="var(--accent)" d="M6.6 2.2c.6-.4 1.4-.3 1.8.3l2.2 3.3c.4.6.3 1.4-.3 1.8L8.6 8.8c.9 2.6 2.9 4.9 5.4 6.3l1.3-1.6c.5-.6 1.3-.7 1.9-.3l3.3 2.1c.6.4.8 1.2.4 1.8l-1.3 2.2c-.6 1-1.8 1.5-2.9 1.2C10 18.8 5 13.6 3.5 7c-.3-1.1.2-2.3 1.2-2.9z"/>
        </svg>
        +12345550199
      </span>
    </div>
  </div>
</section>

<section class="cover cover--red">
  <div class="cover__texture" role="img" aria-label="Faint dark red halftone dot pattern fading from the lower left corner"></div>
  <div class="cover__content">
    <h1 class="cover__headline">More Money In Your Pocket</h1>
    <p class="cover__tagline">With our Low Flat Fee To Sell Your Home</p>
    <div class="cover__contacts">
      <span class="contact">
        <svg class="contact__icon" viewBox="0 0 24 24" aria-hidden="true">
          <circle cx="12" cy="12" r="11" fill="var(--accent)"/>
          <g fill="none" stroke="#040404" stroke-width="1.1">
            <ellipse cx="12" cy="12" rx="4.5" ry="11"/>
            <line x1="12" y1="1" x2="12" y2="23"/>
            <line x1="1" y1="12" x2="23" y2="12"/>
            <path d="M3 6.5h18M3 17.5h18"/>
          </g>
        </svg>
        www.keyvale.com.au
      </span>
      <span class="contact">
        <svg class="contact__icon" viewBox="0 0 24 24" aria-hidden="true">
          <path fill="var(--accent)" d="M6.6 2.2c.6-.4 1.4-.3 1.8.3l2.2 3.3c.4.6.3 1.4-.3 1.8L8.6 8.8c.9 2.6 2.9 4.9 5.4 6.3l1.3-1.6c.5-.6 1.3-.7 1.9-.3l3.3 2.1c.6.4.8 1.2.4 1.8l-1.3 2.2c-.6 1-1.8 1.5-2.9 1.2C10 18.8 5 13.6 3.5 7c-.3-1.1.2-2.3 1.2-2.9z"/>
        </svg>
        +12345550199
      </span>
    </div>
  </div>
</section>

</body>
</html>
```